Business Card - high end, modern health care

Hey designers!

We need a double sided business card for the boutique, cutting edge physical therapy rehabilitation centre in Sydney's Northern Beaches.

With the most qualified physios in the area The Harbourline Motion Clinic does what other physiotherapy practices do not, we take our time with our patients giving them longer appointments, better physios and therefor faster results!

We guarantee that the service people receive at THMC will be unparalleled.

Hence we need a business card to reflect our modern, boutique, high end service. The final design needs to reflect that we are in a class of our own yet with the feel of beachside retreat.

Below I have attached our logo in both blue on white and white on blue. The exact colour is;
and the font that we have used in our logo is Tex Gyre Aventador.

I like the idea of the blue as the main colour as it is more eye catching and our signage onto the main road will be in this blue and in the interest of consistency across marketing the blue needs to be a part of the design. However I would appreciate a few designs onto a wooden background as this is a visual theme within the fitout of the practice.

The design needs to be of standard size (91x55mm).

Target Market(s)

We target people who have an end outcome in mind and those who have had poor experiences with other providers and ensure that everyone gets the care that they deserve with a premium service that is tailored to the individuals circumstances. As a premium service, the target market is highly educated, business and tech savvy with the additional target market of elderly people who have self funded their retirement and see value in paying for the best ongoing rehabilitation to maintain independence.

Industry/Entity Type

Physical Therapy

Contact Information for Business Card

Name, designation( Titled Musculoskeletal Physiotherapist... there will also be those in the company that have multiple designations ie 5 or 6 words long), phone number, email, facebook, instagram, address

Font styles to use
Sans Serif

Colors

Designer to choose colors to be used in the design.

Requirements
Must have
• Front - The logo as large as possible, blue or wooden theme, and all of the important details.
• Back - A blank space/lines on which to write appointment times (no "Appointment, date, time" etc.)
Nice to have
• facebook url
• logos for facebook and instagram
• Mini logos for the phone and email?

```html
<!DOCTYPE html>
<html lang="en">
<head>
<meta charset="utf-8">
<title>The Harbourline Motion Clinic – Business Card</title>
<link href="https://fonts.googleapis.com/css2?family=Montserrat:wght@300;400;500;600;700;800&display=swap" rel="stylesheet">
<style>
  :root{
    --brand-blue:#0b56a8;
    --brand-blue-soft:#2f73bd;
    --paper:#ffffff;
    --line-blue:#3a66b8;
    --backdrop:#e9ecf1;
    --fern-tint:#e4e9f3;
  }
  *{box-sizing:border-box;margin:0;padding:0}
  html,body{width:1200px;height:864px;overflow:hidden;background:var(--backdrop)}
  body{position:relative;font-family:'Montserrat',sans-serif}

  .card{position:absolute;width:540px;height:327px;border-radius:24px;overflow:hidden;
        box-shadow:0 10px 30px rgba(20,40,80,.18)}

  /* ---------- appointment side ---------- */
  .card--appointments{left:60px;top:100px;background:var(--paper)}
  .appt-band{position:absolute;left:0;top:0;width:100%;height:128px;background:var(--brand-blue)}
  .appt-fern{position:absolute;right:0;top:0;width:230px;height:327px;
             background:linear-gradient(160deg,rgba(255,255,255,.35),var(--fern-tint) 55%,rgba(255,255,255,0))}
  .appt-brand{position:absolute;left:34px;top:34px;display:flex;align-items:center;gap:14px;color:var(--paper)}
  .appt-lines{position:absolute;left:112px;right:44px;top:150px}
  .appt-lines span{display:block;height:1px;background:var(--line-blue);margin-bottom:31px}

  .brand-dot{width:58px;height:58px;border-radius:50%;background:var(--paper);flex:none}
  .brand-name{line-height:1}
  .brand-name__main{display:block;font-weight:800;font-size:30px;letter-spacing:.5px}
  .brand-name__sub{display:block;font-weight:400;font-size:15px;letter-spacing:6px;margin-top:5px}

  /* ---------- details side ---------- */
  .card--details{left:600px;top:437px;background:var(--brand-blue);color:var(--paper)}
  .details-art{position:absolute;right:0;top:0;width:320px;height:260px;
               background:radial-gradient(ellipse at 70% 40%,rgba(255,255,255,.9) 0%,rgba(255,255,255,.55) 38%,rgba(255,255,255,0) 72%)}
  .details-brand{position:absolute;left:32px;top:78px}
  .details-brand .brand-name__main{font-size:28px}
  .details-brand .brand-name__sub{font-size:14px;letter-spacing:5.5px}
  .person{position:absolute;left:84px;top:148px}
  .person__name{font-weight:700;font-size:17px;letter-spacing:.3px}
  .person__role{font-weight:600;font-size:10px;letter-spacing:.4px;margin-top:2px}
  .contacts{position:absolute;left:84px;top:196px;font-size:11.5px;font-weight:400;line-height:1}
  .contacts li{list-style:none;display:flex;align-items:center;gap:7px;margin-bottom:6px}
  .contacts svg{width:14px;height:14px;flex:none}
  .address{margin:10px 0 0 0;font-size:11.5px;line-height:1.35}
  .social{position:absolute;left:84px;bottom:20px;display:flex;align-items:center;gap:7px;font-size:12px}
  .social__mark{width:13px;height:13px;border:1.4px solid var(--paper);border-radius:50%}
</style>
</head>
<body>

<section class="card card--appointments" aria-label="Appointment side">
  <div class="appt-band"></div>
  <div class="appt-fern" role="img" aria-label="Faint fern frond decoration"></div>
  <div class="appt-brand">
    <span class="brand-dot"></span>
    <span class="brand-name">
      <span class="brand-name__main">THE HARBOURLINE</span>
      <span class="brand-name__sub">MOTION CLINIC</span>
    </span>
  </div>
  <div class="appt-lines"><span></span><span></span><span></span><span></span><span></span></div>
</section>

<section class="card card--details" aria-label="Contact side">
  <div class="details-art" role="img" aria-label="Large wave and fern decoration in white"></div>
  <div class="details-brand brand-name">
    <span class="brand-name__main">THE HARBOURLINE</span>
    <span class="brand-name__sub">MOTION CLINIC</span>
  </div>
  <div class="person">
    <p class="person__name">DANIEL REYES</p>
    <p class="person__role">MANAGING DIRECTOR</p>
  </div>
  <ul class="contacts">
    <li>
      <svg viewBox="0 0 14 14" fill="none" stroke="#fff" stroke-width="1.2"><circle cx="7" cy="7" r="6.2"/><path d="M4.6 4.2c.4-.4.8-.3 1 .1l.5 1c.1.3 0 .5-.2.7l-.3.3c.4.8 1 1.4 1.8 1.8l.3-.3c.2-.2.4-.3.7-.2l1 .5c.4.2.5.6.1 1-.9.9-2.4.6-3.9-.9S3.7 5.1 4.6 4.2z" fill="#fff" stroke="none"/></svg>
      +612 9000 4182
    </li>
    <li>
      <svg viewBox="0 0 14 14" fill="none" stroke="#fff" stroke-width="1.2"><circle cx="7" cy="7" r="6.2"/><rect x="4.3" y="5.6" width="5.4" height="3" fill="#fff" stroke="none"/><rect x="5" y="3.6" width="4" height="2" stroke-width=".8"/><rect x="5" y="8.4" width="4" height="2" stroke-width=".8"/></svg>
      +612 9000 2751
    </li>
    <li>
      <svg viewBox="0 0 14 14" fill="none" stroke="#fff" stroke-width="1.2"><circle cx="7" cy="7" r="6.2"/><rect x="4" y="4.8" width="6" height="4.4" stroke-width=".9"/><path d="M4 4.8l3 2.5 3-2.5" stroke-width=".9"/></svg>
      info@harbourlinemotion.com
    </li>
    <li class="address">42 Tidewater Lane<br>Collaroy NSW 2097</li>
  </ul>
  <div class="social">
    <span class="social__mark"></span>harbourline.social
    <span>/</span>
    <span class="social__mark"></span>harbourline.photos
  </div>
</section>

</body>
</html>
```